Business Card Design Project

I need a business card design for our new logo, please check the logo at the following link:
https://www.filecrate.net/s/q7rtx2pw9kd41m/FernLoop.png
The address on the business card:
Av. Gervásio Tavares 418 sala 207
Barra da Tijuca, Rio de Janeiro, RJ
CEP: 22714-380
Brasil
Phone: +55 21 86347215
e-mail: osvaldo@fernloop.com.br
Updates
Thank you all for sending your designs, we will not provide feedback because there are too many designs, on December 3 we will pick the best design according to our point of view. Please keep posting.
Osvaldo
Industry/Entity Type
Business
Look and feel
Each slider illustrates characteristics of the customer's brand and the style your logo design should communicate.

```html
<!DOCTYPE html>
<html lang="pt-BR">
<head>
<meta charset="utf-8">
<title>FernLoop – Business Card</title>
<link href="https://fonts.googleapis.com/css2?family=Open+Sans:wght@400;600;700&display=swap" rel="stylesheet">
<style>
  :root {
    --stage: #e9e6e1;
    --paper: #ffffff;
    --ink: #1f2122;
    --yellow: #f6c812;
    --muted: #3a3a3a;
    --light: #ffffff;
  }
  * { box-sizing: border-box; margin: 0; padding: 0; }
  html, body { width: 1200px; height: 450px; overflow: hidden; }
  body {
    background: var(--stage);
    font-family: "Open Sans", Arial, sans-serif;
    position: relative;
  }
  .card {
    position: absolute;
    top: 79px;
    width: 515px;
    height: 292px;
    overflow: hidden;
  }
  .card--front { left: 67px; background: var(--paper); }
  .card--back { left: 619px; background: var(--yellow); }

  .brand {
    position: absolute;
    left: 40px;
    top: 36px;
    width: 190px;
    display: flex;
    flex-direction: column;
    align-items: center;
    gap: 22px;
  }
  .brand__dot {
    width: 78px; height: 78px;
    border-radius: 50%;
    background: var(--yellow);
  }
  .brand__name {
    font-weight: 700;
    font-size: 38px;
    line-height: 1;
    color: var(--ink);
    letter-spacing: -0.5px;
    white-space: nowrap;
  }

  .contact {
    position: absolute;
    right: 83px;
    top: 150px;
    text-align: right;
    font-size: 13px;
    line-height: 18px;
    color: var(--muted);
  }
  .contact__row { display: flex; justify-content: flex-end; align-items: center; gap: 5px; }
  .contact__icon { width: 11px; height: 11px; }

  .band { position: absolute; left: 0; top: 203px; width: 515px; height: 89px; }

  .address {
    position: absolute;
    right: 285px;
    top: 228px;
    text-align: right;
    font-style: normal;
    font-size: 12.5px;
    line-height: 18px;
    color: var(--light);
  }
  .person {
    position: absolute;
    right: 98px;
    top: 236px;
    text-align: right;
  }
  .person__name { font-weight: 700; font-size: 17px; line-height: 20px; color: var(--yellow); }
  .person__title { font-size: 14px; line-height: 18px; color: var(--light); }

  .back-brand {
    position: absolute;
    inset: 0;
    display: flex;
    flex-direction: column;
    align-items: center;
    justify-content: center;
    gap: 18px;
  }
  .back-brand__dot { width: 96px; height: 96px; border-radius: 50%; background: var(--ink); }
  .back-brand__name { font-weight: 700; font-size: 44px; line-height: 1; color: var(--ink); letter-spacing: -0.5px; }
</style>
</head>
<body>

<section class="card card--front" aria-label="Business card front">
  <div class="brand">
    <span class="brand__dot"></span>
    <span class="brand__name">FernLoop</span>
  </div>

  <div class="contact">
    <div class="contact__row">
      <span>+55 21 86347215</span>
      <svg class="contact__icon" viewBox="0 0 12 12" aria-hidden="true">
        <circle cx="6" cy="6" r="5.3" fill="none" stroke="#f6c812" stroke-width="1.2"/>
        <path d="M4 3.2c-.6.4-.7 1.3-.2 2.4.6 1.3 1.7 2.4 2.9 2.9.9.3 1.5 0 1.9-.5L7.5 6.9l-.7.4C6 6.9 5.4 6.2 5 5.4l.4-.7z" fill="#f6c812"/>
      </svg>
    </div>
    <div class="contact__row">
      <span>osvaldo@fernloop.com.br</span>
      <svg class="contact__icon" viewBox="0 0 12 12" aria-hidden="true">
        <rect x="0.5" y="2.5" width="11" height="7.5" rx="1" fill="#f6c812"/>
        <path d="M1 3l5 3.8L11 3" fill="none" stroke="#fff" stroke-width="1"/>
      </svg>
    </div>
  </div>

  <svg class="band" viewBox="0 0 515 89" aria-hidden="true">
    <rect x="0" y="0" width="448" height="3" fill="#f6c812"/>
    <rect x="0" y="5" width="448" height="84" fill="#1f2122"/>
    <polygon points="448,0 515,89 448,89" fill="#f6c812"/>
  </svg>

  <address class="address">
    Av. Gervásio Tavares 418 sala 207<br>
    Barra da Tijuca, Rio de Janeiro, RJ<br>
    CEP: 22714-380, Brasil
  </address>

  <div class="person">
    <div class="person__name">Your Name</div>
    <div class="person__title">Title</div>
  </div>
</section>

<section class="card card--back" aria-label="Business card back">
  <div class="back-brand">
    <span class="back-brand__dot"></span>
    <span class="back-brand__name">FernLoop</span>
  </div>
</section>

</body>
</html>
```